Business Card for Kinesiologist Practitioner

I need a logo and business card designing for a Kinesiologist Practitioner. I would like the card to be double sided. The look and feel of the logo and graphics should depict natural healing and well being. I would like a modern, fresh and contemporary design with a professional style. I have attached some logos and business cards that I liek from other natural health practitioners. I have also attached some logos that I like and a mock up of the business card style. Please however use your own creative input to change any element as you feel appropriate.

I have used the strap line "Quiet Renewal" which I would like underneath the logo. For the logo I like natural objects and possibly with 3 elements in the design as the course I have studied follows a "Open Arc " healing concept (mind, body, soul). Maybe a tree or flower with 3 elements and a representation or suggestion of the human body somehow. You will see from the logos i have uploaded

Industry/Entity Type

Business

Contact Information for Business Card

Please see the mock up attached.

Font styles to use
Serif
Sans Serif

Colors
faa54b
acd036
fbee3d
85cae6

Requirements
Must have
• Note the colours are just suggested colours. Please us your own creative licence.

```html
<!DOCTYPE html>
<html lang="en">
<head>
<meta charset="utf-8">
<title>Quiet Renewal – Business Card</title>
<link href="https://fonts.googleapis.com/css2?family=Raleway:wght@300;400;500;800&display=swap" rel="stylesheet">
<style>
  :root {
    --backdrop: #e6e4df;
    --card-white: #ffffff;
    --leaf-green: #a6cd37;
    --leaf-green-deep: #95c22f;
    --band-green: #0aa04c;
    --ink: #1f1f1f;
    --ink-soft: #3a3a3a;
    --accent: #8cc43c;
  }
  * { margin: 0; padding: 0; box-sizing: border-box; }
  html, body {
    width: 1200px; height: 900px; overflow: hidden;
    background: var(--backdrop);
    font-family: "Raleway", Arial, sans-serif;
  }
  .canvas {
    width: 1200px; height: 900px;
    display: flex; flex-direction: column; align-items: center; justify-content: center;
    gap: 34px;
  }
  .card {
    position: relative;
    width: 700px; height: 400px;
    background: var(--card-white);
    box-shadow: 0 6px 18px rgba(0,0,0,0.18);
    overflow: hidden;
  }

  /* Front */
  .card--front {
    display: flex; flex-direction: column; align-items: center; justify-content: center;
  }
  .wordmark {
    display: flex; align-items: center; gap: 16px;
    color: var(--ink);
    font-weight: 400; font-size: 30px; letter-spacing: 9px;
    text-transform: uppercase;
  }
  .wordmark__dot {
    width: 22px; height: 22px; border-radius: 50%;
    background: var(--leaf-green);
    flex: none;
  }
  .tagline {
    margin-top: 22px;
    font-size: 20px; font-weight: 400; color: var(--ink-soft);
    letter-spacing: 0.5px;
  }
  .tagline__divider { color: var(--accent); margin: 0 6px; }

  /* Back */
  .card--back .backdrop { position: absolute; inset: 0; }
  .identity {
    position: absolute; top: 88px; left: 0; right: 0;
    text-align: center;
  }
  .identity__name {
    font-size: 34px; color: var(--ink); letter-spacing: 0.3px;
  }
  .identity__name strong { font-weight: 800; }
  .identity__name span { font-weight: 400; }
  .identity__role {
    margin-top: 4px;
    font-size: 19px; font-weight: 300; color: var(--card-white);
    letter-spacing: 6px;
  }
  .contact {
    position: absolute; left: 40px; bottom: 42px; width: 370px;
    display: flex; flex-direction: column; align-items: flex-end; gap: 10px;
    color: var(--ink); font-size: 26px; font-weight: 400;
  }
  .contact__row { display: flex; align-items: center; gap: 14px; }
  .contact__icon { width: 24px; height: 24px; flex: none; }
  .back-mark {
    position: absolute; right: 30px; bottom: 48px;
    display: flex; align-items: center; gap: 10px;
    color: var(--ink); font-size: 17px; font-weight: 400; letter-spacing: 4px;
    text-transform: uppercase;
  }
  .back-mark .wordmark__dot { width: 14px; height: 14px; }
</style>
</head>
<body>
<main class="canvas">

  <section class="card card--front" aria-label="Card front">
    <div class="wordmark">
      <span class="wordmark__dot" aria-hidden="true"></span>
      <span class="wordmark__name">Quiet Renewal</span>
    </div>
    <p class="tagline">mind<span class="tagline__divider">|</span>body<span class="tagline__divider">|</span>soul</p>
  </section>

  <section class="card card--back" aria-label="Card back">
    <svg class="backdrop" viewBox="0 0 700 400" preserveAspectRatio="none" aria-hidden="true">
      <defs>
        <radialGradient id="topGlow" cx="0.45" cy="0.05" r="0.8">
          <stop offset="0" stop-color="var(--leaf-green-deep)"/>
          <stop offset="1" stop-color="var(--leaf-green)"/>
        </radialGradient>
      </defs>
      <rect width="700" height="400" fill="url(#topGlow)"/>
      <path d="M0,232 C150,282 300,268 450,226 C560,196 640,184 700,192 L700,400 L0,400 Z" fill="var(--band-green)"/>
      <path d="M0,250 C150,300 300,286 450,244 C560,214 640,202 700,210 L700,400 L0,400 Z" fill="var(--card-white)"/>
    </svg>

    <div class="identity">
      <h1 class="identity__name"><strong>MARA ELSDEN</strong> <span>dip. cert.</span></h1>
      <p class="identity__role">KINESIOLOGIST</p>
    </div>

    <div class="contact">
      <p class="contact__row">0400 517 203
        <svg class="contact__icon" viewBox="0 0 24 24" aria-hidden="true">
          <circle cx="12" cy="12" r="10.5" fill="none" stroke="var(--band-green)" stroke-width="1.8"/>
          <path d="M8.3 6.8c.5-.4 1.1-.3 1.4.2l1 1.6c.3.5.2 1-.2 1.3l-.6.5c.5 1.3 1.5 2.5 2.8 3.2l.5-.6c.4-.4.9-.5 1.3-.2l1.6 1c.5.3.6 1 .2 1.4l-.8.9c-.6.6-1.6.7-2.5.3-2.5-1.1-4.4-3.1-5.4-5.6-.3-.9-.2-1.8.4-2.4z" fill="var(--band-green)"/>
        </svg>
      </p>
      <p class="contact__row">mara@quietrenewal.net
        <svg class="contact__icon" viewBox="0 0 24 24" aria-hidden="true">
          <rect x="2" y="5" width="20" height="14" fill="none" stroke="var(--band-green)" stroke-width="1.8"/>
          <path d="M2 5l10 8 10-8M2 19l7-7M22 19l-7-7" fill="none" stroke="var(--band-green)" stroke-width="1.6"/>
        </svg>
      </p>
    </div>

    <div class="back-mark">
      <span class="wordmark__dot" aria-hidden="true"></span>
      <span>Quiet Renewal</span>
    </div>
  </section>

</main>
</body>
</html>
```